Professional Design for Rap Artist's Promotional Photos

I am promoting my new single "Loud and Sideways" by Prax. I'm a rising rap artist and am working with PR companies on major coverage right now. I need professional and inventive promotional photos to sport with the reviews, articles, and ads.

I have attached some photos I took in front of a green screen. I would like the photos touched up and the backgrounds replaced with something "Loud and Sideways"

I have attached an old Rovaldo photo that I like a lot in regards to the vibes and wacky/crazy look I'm after. He's standing in front of a cartoon background.

Industry/Entity Type

Promotional

Requirements
Must have
• green screen removal
• professional background replacement
Nice to have
• image enhancement in regards to colors, quality, contrast
Should not have
• amateur backgrounds that make the photo blatantly obvious that it is photoshopped

```html
<!DOCTYPE html>
<html lang="en">
<head>
<meta charset="utf-8">
<title>Loud and Sideways by Prax</title>
<link rel="stylesheet" href="https://fonts.googleapis.com/css2?family=Titan+One&family=Questrial&display=swap">
<style>
  :root {
    --paper: #ffffff;
    --frame: #1a1a1a;
    --stone-light: #9d9897;
    --stone-mid: #888382;
    --stone-dark: #767172;
    --title-fill: #ececec;
    --title-shade: #111111;
    --byline: #ffffff;
    --skin: #b08a72;
    --jacket: #8e1f4a;
    --jacket-dark: #6a1636;
    --trousers: #1c1c1c;
  }
  * { margin: 0; padding: 0; box-sizing: border-box; }
  html, body { width: 1200px; height: 1019px; overflow: hidden; background: var(--paper); }
  .poster {
    position: relative;
    width: 1200px;
    height: 1019px;
    background: var(--paper);
  }
  .poster-frame {
    position: absolute;
    left: 3px; top: 3px; right: 3px; bottom: 3px;
    border: 3px solid var(--frame);
  }
  .stone {
    position: absolute;
    left: 88px;
    width: 1040px;
    background:
      radial-gradient(circle at 25% 35%, var(--stone-light) 0, transparent 55%),
      radial-gradient(circle at 80% 65%, var(--stone-light) 0, transparent 50%),
      linear-gradient(135deg, var(--stone-mid), var(--stone-dark) 50%, var(--stone-mid));
  }
  .stone-band { top: 80px; height: 101px; }
  .stone-panel { top: 240px; height: 688px; }
  .artist-photo {
    position: absolute;
    left: 775px;
    top: 140px;
    width: 290px;
    height: 860px;
    border-radius: 90px 90px 16px 16px;
    background: linear-gradient(180deg,
      var(--skin) 0%,
      var(--skin) 12%,
      var(--jacket) 18%,
      var(--jacket-dark) 55%,
      var(--trousers) 62%,
      var(--trousers) 100%);
  }
  .title-block { font-weight: 400; }
  .title {
    position: absolute;
    font-family: "Titan One", "Arial Black", sans-serif;
    font-weight: 400;
    color: var(--title-fill);
    line-height: 1;
    white-space: nowrap;
    text-shadow:
      -3px 3px 0 var(--title-shade),
      -6px 6px 0 var(--title-shade),
      -9px 9px 0 var(--title-shade),
      -12px 12px 0 var(--title-shade),
      -2px -2px 0 var(--title-shade),
      2px -2px 0 var(--title-shade),
      2px 2px 0 var(--title-shade);
  }
  .title-loud { left: 250px; top: 360px; font-size: 152px; }
  .title-and { left: 395px; top: 520px; font-size: 130px; }
  .title-sideways { left: 240px; top: 675px; font-size: 90px; }
  .byline {
    position: absolute;
    left: 370px;
    top: 822px;
    font-family: "Questrial", "Century Gothic", sans-serif;
    font-size: 78px;
    color: var(--byline);
    line-height: 1;
    white-space: nowrap;
  }
</style>
</head>
<body>
  <main class="poster">
    <div class="poster-frame"></div>
    <div class="stone stone-band" role="img" aria-label="Grey speckled stone texture band"></div>
    <div class="stone stone-panel" role="img" aria-label="Grey speckled stone texture backdrop"></div>
    <div class="artist-photo" role="img" aria-label="Photo of the artist in sunglasses, a maroon velvet blazer and black jeans, holding a keytar"></div>
    <h1 class="title-block">
      <span class="title title-loud">Loud</span>
      <span class="title title-and">and</span>
      <span class="title title-sideways">Sideways</span>
    </h1>
    <p class="byline">by Prax</p>
  </main>
</body>
</html>
```